Design a (20.4 x 10.14) Banner that says - Keep Hope Rising From Harvest Crown TV Family

We want a design (20.4 x 10.14) with the words 'Keep Hope Rising' as the main text and 'From Harvest Crown TV Family' underneath. For 'Harvest Crown TV', we'd like you to use the logo which can be found in the image attached.

The image attached is just an example but please let your creative juices flow!

Target Market(s)

Christian

Industry/Entity Type

Christian

Requirements
Must have
• Must have the words 'Keep Hope Rising' and 'From Harvest Crown TV Family'.

```html
<!DOCTYPE html>
<html lang="en">
<head>
<meta charset="utf-8">
<title>Keep Hope Rising – Harvest Crown TV</title>
<link rel="stylesheet" href="https://fonts.googleapis.com/css2?family=Alfa+Slab+One&family=Playball&family=Pinyon+Script&display=swap">
<style>
  :root {
    --sky-deep: #1b2536;
    --sky-mid: #3a4250;
    --cloud: #5c6068;
    --frame-blue: #1010f0;
    --hope-blue: #0b0bff;
    --script-white: #fffdf2;
    --glow-warm: #fff3b0;
    --brand-violet: #5a4fd0;
    --heart-red: #e0102a;
    --heart-blue: #3b4aa8;
  }
  * { margin: 0; padding: 0; box-sizing: border-box; }
  html, body { width: 1200px; height: 597px; overflow: hidden; background: var(--sky-deep); }
  .banner { position: relative; width: 1200px; height: 597px; overflow: hidden; }
  .sky-photo {
    position: absolute; inset: 0;
    background:
      radial-gradient(ellipse 55% 60% at 45% 45%, var(--cloud) 0%, transparent 70%),
      radial-gradient(ellipse 40% 40% at 80% 20%, #4a4f5a 0%, transparent 70%),
      linear-gradient(160deg, var(--sky-deep) 0%, var(--sky-mid) 50%, #262d3b 100%);
  }
  .frame {
    position: absolute; left: 41px; top: 27px; width: 1112px; height: 538px;
    border: 2px solid var(--frame-blue);
  }
  .heart { position: absolute; left: 553px; top: 58px; width: 88px; height: 100px; }
  .brand {
    position: absolute; right: 72px; top: 58px;
    font-family: "Alfa Slab One", serif; font-size: 20px; color: var(--brand-violet);
    letter-spacing: 0.5px;
  }
  .headline { font-weight: normal; }
  .script {
    position: absolute; z-index: 2; font-family: "Playball", cursive; color: var(--script-white);
    text-shadow: 0 0 6px var(--glow-warm), 0 0 14px rgba(255, 243, 176, .6);
    line-height: 1; white-space: nowrap;
  }
  .title-keep { left: 250px; top: 100px; font-size: 120px; }
  .title-hope {
    position: absolute; z-index: 1; left: 0; right: 0; top: 212px; text-align: center;
    font-family: "Alfa Slab One", serif; font-size: 145px; line-height: 1;
    color: var(--hope-blue); letter-spacing: -2px;
    text-shadow: 0 0 10px rgba(40, 40, 255, .7);
  }
  .title-rising { left: 712px; top: 298px; font-size: 115px; }
  .sign-off {
    position: absolute; left: 0; right: 0; top: 466px; text-align: center;
    font-family: "Pinyon Script", cursive; color: var(--script-white);
    font-size: 30px; line-height: 1.15;
  }
  .sign-off-lead { display: inline-block; border-bottom: 1.5px solid var(--script-white); padding: 0 10px 2px; }
  .sign-off-name { display: block; margin-top: 4px; }
</style>
</head>
<body>
  <main class="banner">
    <div class="sky-photo" role="img" aria-label="Photo of red and white heart balloons floating into a cloudy dusk sky"></div>
    <div class="frame"></div>
    <svg class="heart" viewBox="0 0 94 106" aria-hidden="true">
      <defs>
        <linearGradient id="heartFill" x1="0" y1="0" x2="1" y2="0">
          <stop offset="0" stop-color="var(--heart-blue)"/>
          <stop offset="0.6" stop-color="var(--heart-red)"/>
        </linearGradient>
      </defs>
      <path d="M47 104 C20 72 2 52 2 28 C2 12 14 2 27 2 C37 2 44 9 47 18 C50 9 57 2 67 2 C80 2 92 12 92 28 C92 52 74 72 47 104 Z"
            fill="url(#heartFill)" stroke="#4a3fb0" stroke-width="2"/>
    </svg>
    <div class="brand">Harvest Crown TV</div>
    <h1 class="headline">
      <span class="script title-keep">Keep</span>
      <span class="title-hope">HOPE</span>
      <span class="script title-rising">Rising</span>
    </h1>
    <p class="sign-off">
      <span class="sign-off-lead">From</span>
      <span class="sign-off-name">Harvest Crown TV Family</span>
    </p>
  </main>
</body>
</html>
```